Brannigan Ashcroft LLC. custom built/handcrafted

I am recent small business owner looking to sell my art(drawings) and woodworking projects from my home. I have a very rough draft of a simple card design created on a simple digital program. I was hoping for a fancier lettering on the initial letters (BA). More of a calligraphy style. Also, the yellow border around the logo I would like to be a gold foil look. For it to be shiny or reflective look and to keep the other letters black with a consistent font on the card and the card white.

Target Market(s)

Local and neighboring cities

Industry/Entity Type

Art (drawing)/Woodworking

Contact Information for Business Card

My email tpashcroft@mailvane.net, phone number 949-517-3068. In the files provided it has a yellow border around the logo and I was looking to make that a gold foil.

Font styles to use
Serif
Decorative
Script

Requirements
Nice to have
• symbols for having a Facebook and Instagram

```html
<!DOCTYPE html>
<html lang="en">
<head>
<meta charset="utf-8">
<title>Brannigan Ashcroft LLC. – Business Card</title>
<link rel="stylesheet" href="https://fonts.googleapis.com/css2?family=Poppins:wght@400;500;700&display=swap">
<style>
  :root {
    --backdrop: #ecebe9;
    --card: #ffffff;
    --ink: #111111;
    --ink-soft: #3a3a3a;
    --gold: #c49a22;
  }
  * { box-sizing: border-box; margin: 0; padding: 0; }
  html, body { width: 1200px; height: 763px; overflow: hidden; }
  body {
    background: var(--backdrop);
    font-family: "Poppins", sans-serif;
    color: var(--ink);
    position: relative;
  }
  .card {
    position: absolute;
    left: 320px;
    width: 560px;
    height: 320px;
    background: var(--card);
    box-shadow: 0 6px 18px rgba(0,0,0,.12);
    overflow: hidden;
  }
  .card--front { top: 41px; }
  .card--back { top: 401px; }
  .foil { position: absolute; inset: 0; width: 100%; height: 100%; }

  .brand {
    position: absolute;
    left: 0; right: 0; top: 146px;
    display: flex; align-items: center; justify-content: center; gap: 10px;
  }
  .brand__dot {
    width: 12px; height: 12px; border-radius: 50%;
    background: var(--gold); flex: none;
  }
  .brand__name {
    font-weight: 700;
    font-size: 22px;
    letter-spacing: 1px;
    line-height: 1;
    color: var(--ink);
  }

  .owner {
    position: absolute;
    left: 40px; top: 150px;
  }
  .owner__name {
    font-weight: 700;
    font-size: 17px;
    letter-spacing: 3px;
  }
  .owner__role {
    font-weight: 500;
    font-size: 12px;
    letter-spacing: 1.5px;
    color: var(--gold);
    margin-top: 2px;
  }
  .contacts {
    list-style: none;
    margin-top: 14px;
    font-size: 11px;
    color: var(--ink-soft);
  }
  .contacts li {
    display: flex; align-items: center; gap: 8px;
    height: 17px;
  }
  .contacts svg { width: 11px; height: 11px; flex: none; }
  .contacts .social {
    width: 11px; height: 11px; border-radius: 50%;
    background: var(--gold); flex: none;
  }
</style>
</head>
<body>
<svg width="0" height="0" style="position:absolute" aria-hidden="true">
  <defs>
    <linearGradient id="gold-foil" x1="0" y1="0" x2="1" y2="1">
      <stop offset="0" stop-color="#9a7414"/>
      <stop offset=".3" stop-color="#e8c65a"/>
      <stop offset=".55" stop-color="#c49a22"/>
      <stop offset=".8" stop-color="#f0d57a"/>
      <stop offset="1" stop-color="#a67d18"/>
    </linearGradient>
  </defs>
</svg>

<section class="card card--front" aria-label="Card front">
  <svg class="foil" viewBox="0 0 560 320" role="img" aria-label="Gold foil brush strokes along the card edges">
    <path d="M0 0 H150 L180 18 L140 40 L60 52 L0 60 Z" fill="url(#gold-foil)"/>
    <path d="M0 118 L55 112 L78 140 L70 190 L40 218 L0 222 Z" fill="url(#gold-foil)"/>
    <path d="M560 108 L470 100 L440 130 L455 175 L500 200 L560 196 Z" fill="url(#gold-foil)"/>
    <path d="M560 262 L470 246 L400 258 L430 290 L560 320 Z" fill="url(#gold-foil)"/>
  </svg>
  <div class="brand">
    <span class="brand__dot" aria-hidden="true"></span>
    <span class="brand__name">Brannigan Ashcroft LLC.</span>
  </div>
</section>

<section class="card card--back" aria-label="Card back">
  <svg class="foil" viewBox="0 0 560 320" role="img" aria-label="Gold foil brush stroke sweeping diagonally across the card">
    <path d="M20 0 H300 L420 50 L560 90 V260 L500 250 L430 200 L330 150 L230 110 L100 70 L30 40 Z" fill="url(#gold-foil)"/>
  </svg>
  <div class="owner">
    <div class="owner__name">TOBIAS P. ASHCROFT</div>
    <div class="owner__role">OWNER</div>
    <ul class="contacts">
      <li>
        <svg viewBox="0 0 24 24" aria-hidden="true"><path fill="var(--gold)" d="M6.6 10.8a15 15 0 0 0 6.6 6.6l2.2-2.2a1 1 0 0 1 1-.25 11 11 0 0 0 3.6.6 1 1 0 0 1 1 1V20a1 1 0 0 1-1 1A17 17 0 0 1 3 4a1 1 0 0 1 1-1h3.5a1 1 0 0 1 1 1 11 11 0 0 0 .6 3.6 1 1 0 0 1-.25 1z"/></svg>
        949-517-3068
      </li>
      <li>
        <svg viewBox="0 0 24 24" aria-hidden="true"><rect x="2" y="5" width="20" height="14" rx="2" fill="var(--gold)"/><path d="M3 6l9 7 9-7" fill="none" stroke="#fff" stroke-width="2"/></svg>
        tpashcroft@mailvane.net
      </li>
      <li><span class="social" aria-hidden="true"></span></li>
      <li><span class="social" aria-hidden="true"></span></li>
    </ul>
  </div>
</section>
</body>
</html>
```